Professional Sales Business looking for inspirational poster

I need an inspirational poster design for sales professionals, targeted around the phrase "Win Fast, Lose Fast". The style of the poster will be primarily minimalistic and flat with the main focus being on the phrase, however, any graphics or creative font and background styles are encouraged. Color choice is up to you.

Design Specs:
Vector files are best. If creating a vector file isn't possible, 150dpi raster images (at actual size or bigger) are good too. The poster must be in a portrait layout and scalable to the sizes of 18" X 24" and 24" X 36". Please convert all text to outlines.

Please msg me if you have any additional questions.

```html
<!DOCTYPE html>
<html lang="en">
<head>
<meta charset="utf-8">
<title>Win Fast Lose Fast — Poster</title>
<link rel="stylesheet" href="https://fonts.googleapis.com/css2?family=Open+Sans:wght@800&display=swap">
<style>
  :root {
    --backdrop: #f1f1f1;
    --poster-green: #27453a;
    --headline-red: #b9141b;
    --headline-white: #ffffff;
    --clock-white: #fbfbfb;
    --bell-orange: #d9822b;
    --hand-red: #c0151c;
  }
  html, body {
    margin: 0;
    padding: 0;
    overflow: hidden;
  }
  body {
    width: 1200px;
    height: 1200px;
    background: var(--backdrop);
    position: relative;
  }
  .poster {
    position: absolute;
    left: 176px;
    top: 35px;
    width: 848px;
    height: 1130px;
    background: var(--poster-green);
  }
  .poster-art {
    position: absolute;
    inset: 0;
    width: 848px;
    height: 1130px;
  }
  .headline {
    font-family: "Open Sans", "Arial Black", sans-serif;
    font-weight: 800;
    font-size: 160px;
    letter-spacing: -3px;
  }
  .headline-win { fill: var(--headline-red); }
  .headline-lose { fill: var(--headline-white); }
</style>
</head>
<body>
  <main class="poster">
    <svg class="poster-art" viewBox="0 0 848 1130" xmlns="http://www.w3.org/2000/svg">
      <defs>
        <linearGradient id="clock-tone" x1="0" y1="0" x2="1" y2="1">
          <stop offset="0" stop-color="#ffffff"/>
          <stop offset="1" stop-color="#e6e6e6"/>
        </linearGradient>
        <linearGradient id="fallen-parts-tone" x1="0" y1="0" x2="1" y2="0">
          <stop offset="0" stop-color="#c0151c"/>
          <stop offset="0.5" stop-color="#d9822b"/>
          <stop offset="1" stop-color="#c0151c"/>
        </linearGradient>
      </defs>

      <g class="headline" text-anchor="end">
        <text class="headline-win" x="558" y="380">WIN</text>
        <text class="headline-win" x="558" y="524">FAST</text>
        <text class="headline-lose" x="558" y="668">LOSE</text>
        <text class="headline-lose" x="558" y="800">FAST</text>
      </g>

      <rect class="clock-illustration" x="562" y="542" width="138" height="282" rx="10"
            fill="url(#clock-tone)" role="img"
            aria-label="Illustration of half an alarm clock emerging from the lettering"/>

      <rect class="fallen-parts-illustration" x="430" y="800" width="230" height="66" rx="8"
            fill="url(#fallen-parts-tone)" role="img"
            aria-label="Illustration of a fallen orange alarm bell and red clock hands on the floor"/>
    </svg>
  </main>
</body>
</html>
```